Business Card Design For Marketing Agnecy LVT

Need business card design for marketing agency.

Dorian Pell
President, CEO
1-555-304-2917
dorian@lumenvaletrewards.net
www.LumenValeTrewards.biz

Back Side:
Boost Sales Using Rewards, Incentives & Giveaways
Get A Free Sample Package

Target Market(s)

B2B

Industry/Entity Type

Marketing

Contact Information for Business Card

Dorian Pell
President, CEO
1-555-304-2917

Back Side:
Get A Free Sample Package

Please note that my current url is OLD DESIGN. I am working on new design and want the business card to match color themes at least on new site. Here is the demo link for new site so you can see the colors I use, etc.

http://pagekilnstudio.example/qx/dorian/lvt_final/index.html

Requirements
Must have
• Please note that my current url is OLD DESIGN. I am working on new design and want the business card to match color themes at least on new site. Here is the demo link for new site so you can see the colors I use, etc.

Nice to have

Should not have

```html
<!DOCTYPE html>
<html lang="en">
<head>
<meta charset="utf-8">
<title>LVT Business Card</title>
<link href="https://fonts.googleapis.com/css2?family=Montserrat:ital,wght@0,400;0,500;0,700;0,800;1,800&display=swap" rel="stylesheet">
<style>
  :root {
    --brand-blue: #1f6fb8;
    --brand-blue-deep: #1a5e9e;
    --ink-gray: #4a4d52;
    --paper: #f4f4f4;
    --stage: #e2e3e5;
    --white: #ffffff;
  }
  * { box-sizing: border-box; margin: 0; padding: 0; }
  html, body { width: 1200px; height: 1126px; overflow: hidden; }
  body {
    background: var(--stage);
    font-family: "Montserrat", sans-serif;
    position: relative;
  }
  .card {
    position: absolute;
    left: 220px;
    width: 760px;
    height: 434px;
    box-shadow: 0 6px 18px rgba(0,0,0,0.18);
    overflow: hidden;
  }
  /* Back side */
  .card-back {
    top: 100px;
    background: linear-gradient(160deg, var(--brand-blue) 0%, var(--brand-blue-deep) 100%);
    color: var(--white);
    text-align: center;
  }
  .back-mark {
    position: absolute;
    top: 84px; left: 0; right: 0;
    display: flex; justify-content: center; align-items: center; gap: 14px;
    color: var(--brand-blue-deep);
    font-weight: 800;
    font-size: 96px;
    letter-spacing: 2px;
  }
  .back-mark .dot {
    width: 22px; height: 22px; border-radius: 50%;
    background: var(--brand-blue-deep);
  }
  .offer {
    position: absolute;
    top: 262px; left: 0; right: 0;
    font-size: 38px;
    font-weight: 400;
    letter-spacing: 1px;
    text-transform: uppercase;
  }
  .offer strong { font-weight: 800; }
  .offer-sub {
    position: absolute;
    top: 318px; left: 0; right: 0;
    font-size: 17px;
    font-weight: 500;
    letter-spacing: 0.5px;
  }
  /* Front side */
  .card-front {
    top: 592px;
    background: var(--paper);
  }
  .front-mark {
    position: absolute;
    top: 62px; left: 0; right: 0;
    display: flex; justify-content: center; align-items: center; gap: 14px;
    color: var(--brand-blue);
    font-weight: 800;
    font-size: 104px;
    letter-spacing: 2px;
  }
  .front-mark .dot {
    width: 22px; height: 22px; border-radius: 50%;
    background: var(--brand-blue);
  }
  .front-mark-rule {
    position: absolute;
    top: 196px; left: 268px;
    width: 224px; height: 2px;
    background: var(--brand-blue);
  }
  .identity {
    position: absolute;
    top: 280px; left: 60px;
    width: 256px;
    text-align: right;
  }
  .identity .name {
    color: var(--brand-blue);
    font-weight: 800;
    font-style: italic;
    font-size: 27px;
    text-transform: uppercase;
    letter-spacing: 0.3px;
  }
  .identity .role {
    color: var(--ink-gray);
    font-size: 19px;
    margin-top: 4px;
  }
  .divider {
    position: absolute;
    top: 272px; left: 340px;
    width: 3px; height: 84px;
    background: var(--brand-blue);
  }
  .contacts {
    position: absolute;
    top: 272px; left: 366px;
    list-style: none;
    color: var(--ink-gray);
    font-size: 18px;
  }
  .contacts li {
    display: flex; align-items: center; gap: 12px;
    height: 28px;
  }
  .contacts svg { width: 17px; height: 17px; flex: none; }
  .front-band {
    position: absolute;
    left: 0; right: 0; bottom: 0;
    height: 14px;
    background: var(--brand-blue);
  }
</style>
</head>
<body>
  <section class="card card-back" aria-label="Card back side">
    <div class="back-mark"><span>LVT</span><span class="dot"></span></div>
    <p class="offer">Get a <strong>Free Sample</strong> Package</p>
    <p class="offer-sub">Boost Sales Using Rewards, Incentives &amp; Giveaways</p>
  </section>

  <section class="card card-front" aria-label="Card front side">
    <div class="front-mark"><span>LVT</span><span class="dot"></span></div>
    <div class="front-mark-rule"></div>

    <div class="identity">
      <p class="name">Dorian Pell</p>
      <p class="role">President, CEO</p>
    </div>
    <div class="divider"></div>

    <ul class="contacts">
      <li>
        <svg viewBox="0 0 24 24" aria-hidden="true"><path fill="#1f6fb8" d="M6.6 10.8a15.1 15.1 0 0 0 6.6 6.6l2.2-2.2a1 1 0 0 1 1-.25 11.4 11.4 0 0 0 3.6.57 1 1 0 0 1 1 1V20a1 1 0 0 1-1 1A17 17 0 0 1 3 4a1 1 0 0 1 1-1h3.5a1 1 0 0 1 1 1c0 1.25.2 2.45.57 3.6a1 1 0 0 1-.25 1z"/></svg>
        1-555-304-2917
      </li>
      <li>
        <svg viewBox="0 0 24 24" aria-hidden="true"><rect x="2" y="5" width="20" height="14" rx="1.5" fill="#1f6fb8"/><path d="M3 6l9 7 9-7" fill="none" stroke="#f4f4f4" stroke-width="1.8"/></svg>
        dorian@lumenvaletrewards.net
      </li>
      <li>
        <svg viewBox="0 0 24 24" aria-hidden="true"><g fill="none" stroke="#1f6fb8" stroke-width="2"><circle cx="12" cy="12" r="9.5"/><ellipse cx="12" cy="12" rx="4.2" ry="9.5"/><path d="M2.5 12h19M4 7h16M4 17h16"/></g></svg>
        www.LumenValeTrewards.biz
      </li>
    </ul>
    <div class="front-band"></div>
  </section>
</body>
</html>
```